Looking for a modern, Professional business card design

We have a simple business card, but are looking for a more modern, professional look. A sample of the basic card is attached as well as the logo. We would also like to add that we offer:
Struggling with your finances?
- Learn to become debt free
- Discover the power of cash
- Control your money instead of it controlling you
Let us help you achieve a new level of financial freedom!
Also, we would like to have a "SPECIAL OFFER!: FREE 30 minute consultation"
Financial Planning

```html
<!DOCTYPE html>
<html lang="en">
<head>
<meta charset="utf-8">
<title>Northpine Coaching – Business Card</title>
<link href="https://fonts.googleapis.com/css2?family=Open+Sans:wght@400;600;700;800&family=Open+Sans+Condensed:wght@700&display=swap" rel="stylesheet">
<style>
  :root {
    --backdrop: #3b3431;
    --card-white: #fbfbfa;
    --card-black: #1e1e1e;
    --green: #5db53a;
    --green-bright: #7cc441;
    --green-dark: #3f8f27;
    --ink: #2b2b2b;
    --white: #ffffff;
  }
  * { box-sizing: border-box; margin: 0; padding: 0; }
  html, body { width: 1200px; height: 844px; overflow: hidden; }
  body {
    background: var(--backdrop);
    font-family: "Open Sans", Arial, sans-serif;
    position: relative;
  }
  .card {
    position: absolute;
    top: 268px;
    width: 540px;
    height: 309px;
    border-radius: 3px;
    box-shadow: 0 10px 26px rgba(0,0,0,.45);
    overflow: hidden;
  }

  /* Front side */
  .card-front { left: 40px; background: var(--card-white); color: var(--ink); }
  .brand {
    position: absolute; left: 34px; top: 40px;
    display: flex; align-items: center; gap: 12px;
  }
  .brand-dot { width: 34px; height: 34px; border-radius: 50%; background: var(--green); flex: none; }
  .brand-name {
    font-weight: 800; font-size: 23px; line-height: 1.05; color: var(--ink);
    letter-spacing: .5px; text-transform: uppercase;
  }
  .brand-tagline {
    position: absolute; left: 80px; top: 84px;
    font-size: 10px; color: var(--green-dark);
  }
  .person { position: absolute; left: 34px; top: 150px; }
  .person-name { font-size: 19px; font-weight: 600; color: var(--green); }
  .person-role { font-size: 13px; color: var(--ink); margin-top: 2px; }
  .contacts { position: absolute; left: 34px; top: 212px; list-style: none; }
  .contacts li {
    display: flex; align-items: center; gap: 10px;
    font-size: 13.5px; line-height: 26px; color: var(--ink);
  }
  .contacts svg { width: 13px; height: 13px; fill: var(--green); flex: none; }

  /* Back side */
  .card-back { left: 620px; background: var(--card-black); color: var(--white); }
  .offer {
    position: absolute; left: 0; top: 0; width: 218px; height: 100%;
    display: flex; flex-direction: column; align-items: center; justify-content: center;
    text-transform: uppercase; text-align: center;
  }
  .offer-label { font-weight: 700; font-size: 15px; letter-spacing: .3px; }
  .offer-free { font-family: "Open Sans Condensed", "Open Sans", sans-serif; font-weight: 700; font-size: 60px; line-height: .95; }
  .offer-number { font-family: "Open Sans Condensed", "Open Sans", sans-serif; font-weight: 700; font-size: 92px; line-height: .9; }
  .offer-unit { font-family: "Open Sans Condensed", "Open Sans", sans-serif; font-weight: 700; font-size: 40px; line-height: 1; }
  .offer-note { font-size: 15px; font-weight: 600; margin-top: 8px; }
  .divider { position: absolute; left: 218px; top: 0; width: 2px; height: 100%; background: var(--green-dark); }
  .pitch { position: absolute; left: 244px; top: 30px; right: 26px; }
  .pitch-heading {
    color: var(--green-bright); font-weight: 700; font-size: 23px; line-height: 1.3;
  }
  .pitch-heading span { display: block; border-bottom: 1.5px solid var(--green-bright); padding-bottom: 1px; width: fit-content; }
  .pitch-list { list-style: none; margin-top: 12px; font-size: 12.5px; line-height: 20px; color: var(--white); }
  .pitch-call {
    margin-top: 28px; color: var(--green-bright); font-weight: 700;
    font-size: 12.5px; line-height: 20px; text-transform: uppercase;
  }
</style>
</head>
<body>

<section class="card card-front">
  <div class="brand">
    <span class="brand-dot"></span>
    <span class="brand-name">Northpine Coaching</span>
  </div>
  <p class="brand-tagline">Practical steps toward a calmer budget</p>

  <div class="person">
    <h1 class="person-name">Daniel R. Hayes</h1>
    <p class="person-role">Personal Financial Coach</p>
  </div>

  <ul class="contacts">
    <li>
      <svg viewBox="0 0 24 24" aria-hidden="true"><path d="M6.6 10.8a15.1 15.1 0 0 0 6.6 6.6l2.2-2.2a1 1 0 0 1 1-.25 11.4 11.4 0 0 0 3.6.57 1 1 0 0 1 1 1V20a1 1 0 0 1-1 1A17 17 0 0 1 3 4a1 1 0 0 1 1-1h3.5a1 1 0 0 1 1 1c0 1.25.2 2.45.57 3.57a1 1 0 0 1-.25 1z"/></svg>
      (205) 555-0147
    </li>
    <li>
      <svg viewBox="0 0 24 24" aria-hidden="true"><path d="M2 5h20v14H2z M2 5l10 8 10-8" /></svg>
      daniel@steadymoneypath.com
    </li>
    <li>
      <svg viewBox="0 0 24 24" aria-hidden="true"><circle cx="12" cy="12" r="10"/></svg>
      www.steadymoneypath.com
    </li>
  </ul>
</section>

<section class="card card-back">
  <div class="offer">
    <p class="offer-label">Special Offer!:</p>
    <p class="offer-free">Free</p>
    <p class="offer-number">30</p>
    <p class="offer-unit">Minute</p>
    <p class="offer-note">Consultation</p>
  </div>
  <div class="divider"></div>
  <div class="pitch">
    <h2 class="pitch-heading"><span>Struggling with</span><span>your finances?</span></h2>
    <ul class="pitch-list">
      <li>Learn to become debt free</li>
      <li>Discover the power of cash</li>
      <li>Control your money</li>
      <li>instead of it controlling you</li>
    </ul>
    <p class="pitch-call">Let us help you achieve a new<br>level of financial freedom!</p>
  </div>
</section>

</body>
</html>
```